We need a single web page design for a promotion. This page will acts as a landing page for users. Please provide us with a cutting edge design. I have attached a previous design used a couple of years ago.

Link: http://www.brightkettlestudio.example/freegift/

The Start Here box needs to look like this:

-Start Here (heading) 
-A box for email addresses to be entered
-Then a check box with "Yes, I have read and agree to the Privacy Policy and agree to receive email marketing from Bright Kettle Studio and acknowledge that I will receive special email offers from our marketing partners, including the Harbor Ledger newsletter."
-A submit button 

All of this information needs to be in one box please.  And please feel free to contact me if you have any questions about this. 

Target Market(s)

Middle aged women (housewives)

Requirements
Must have
• Images must reflect the "500 Photo Prints". The only fields that are necessary are a box for email and a submit button.
Should not have
• The word FREE anywhere on the page

```html
<!DOCTYPE html>
<html lang="en">
<head>
<meta charset="utf-8">
<title>500 Photo Prints – Bright Kettle Studio</title>
<link rel="stylesheet" href="https://fonts.googleapis.com/css2?family=Questrial&family=Dancing+Script:wght@700&family=Arimo&display=swap">
<style>
  :root {
    --ink: #000000;
    --panel: #0b0b0b;
    --lime: #5cf03a;
    --lime-deep: #2fb51a;
    --grey-text: #d6d6d6;
    --white: #ffffff;
    --sky-top: #3f74c9;
    --sky-mid: #9cc0ea;
    --haze: #eef3f6;
    --grass: #a8d24a;
    --grass-deep: #6f9e2a;
    --divider: #3c6a2a;
  }
  * { box-sizing: border-box; margin: 0; padding: 0; }
  html, body { width: 1200px; height: 874px; overflow: hidden; background: var(--ink); }
  .page { position: relative; width: 1200px; height: 874px; overflow: hidden; font-family: "Questrial", sans-serif; }

  .backdrop {
    position: absolute; inset: 0;
    background: linear-gradient(180deg, var(--sky-top) 0%, var(--sky-mid) 35%, var(--haze) 68%, var(--grass) 84%, var(--grass-deep) 100%);
  }
  .top-band { position: absolute; left: 0; top: 0; width: 1200px; height: 38px; background: var(--ink); }

  .headline {
    position: absolute; left: 146px; top: 0; width: 917px; height: 118px;
    background: var(--ink); border-radius: 0 0 12px 12px;
    display: flex; align-items: center; padding-left: 40px; color: var(--grey-text);
  }
  .headline .word { font-size: 42px; }
  .headline .count { font-size: 68px; color: var(--lime); margin: 0 16px 0 32px; letter-spacing: -1px; }
  .headline .tagline {
    font-family: "Dancing Script", cursive; font-size: 52px; color: var(--lime);
    margin-left: 72px; text-shadow: 0 0 18px rgba(92,240,58,.35);
  }

  .signup {
    position: absolute; left: 144px; top: 145px; width: 244px; height: 366px;
    background: var(--panel); border: 2px solid var(--ink); border-radius: 12px; overflow: hidden;
  }
  .signup-title {
    height: 66px; display: flex; align-items: center; justify-content: center;
    background: linear-gradient(180deg, #6ff44a 0%, var(--lime-deep) 55%, #0c2a06 100%);
    color: #e8e8e8; font-size: 32px; border-bottom: 2px solid var(--ink);
  }
  .email-field {
    display: block; margin: 13px 0 0 5px; width: 229px; height: 42px;
    background: var(--white); border: 2px solid #b5b5b5;
    font-family: "Arimo", sans-serif; font-size: 13px; color: #222; padding-left: 8px; line-height: 38px;
  }
  .consent {
    margin: 16px 8px 0 8px; font-family: "Arimo", sans-serif; font-size: 12.5px; line-height: 19px; color: var(--white);
  }
  .consent .box {
    display: inline-block; width: 11px; height: 11px; background: var(--white);
    border: 1px solid #888; vertical-align: -1px; margin-right: 4px;
  }
  .submit {
    position: absolute; left: 17px; top: 288px; width: 208px; height: 54px;
    border: 2px solid #9bf27a; border-radius: 9px;
    background: linear-gradient(180deg, #8ef860 0%, var(--lime) 45%, var(--lime-deep) 100%);
    display: flex; align-items: center; padding-left: 38px; color: var(--white); font-size: 27px;
  }
  .submit svg { position: absolute; right: 26px; top: 12px; }

  .gallery .shot {
    position: absolute; width: 168px; height: 108px; border: 3px solid var(--white);
    box-shadow: 0 1px 3px rgba(0,0,0,.3);
  }
  .shot.s1 { left: 524px; top: 140px; background: linear-gradient(135deg, #c9d8e6, #e0b898); }
  .shot.s2 { left: 714px; top: 140px; background: linear-gradient(180deg, #8fbf4a, #e7c830); }
  .shot.s3 { left: 902px; top: 140px; background: linear-gradient(135deg, #e8c8a8, #9a78b8); }
  .shot.s4 { left: 624px; top: 262px; background: linear-gradient(180deg, #3d8ad8, #5fae32); }
  .shot.s5 { left: 815px; top: 262px; background: linear-gradient(135deg, #cfe0ea, #d8b090); }

  .bottom-band { position: absolute; left: 0; top: 836px; width: 1200px; height: 38px; background: var(--ink); }
  .features {
    position: absolute; left: 136px; top: 788px; width: 917px; height: 86px;
    background: var(--ink); border-radius: 12px 12px 0 0; display: flex;
  }
  .feature {
    flex: 1; display: flex; flex-direction: column; align-items: center; justify-content: center;
    color: #e6e6e6; text-align: center;
    background: radial-gradient(ellipse 45% 40% at 50% 55%, rgba(92,240,58,.22), transparent);
  }
  .feature + .feature { border-left: 1px solid var(--divider); }
  .feature.f1 { flex: 0 0 291px; }
  .feature.f2 { flex: 0 0 321px; }
  .feature .small { font-size: 16px; }
  .feature .large { font-size: 22px; margin-top: 2px; }
</style>
</head>
<body>
<div class="page">
  <div class="backdrop" role="img" aria-label="Photo of a bright blue sky with clouds over a grassy meadow, two women in sun hats and red and yellow tops seen from behind"></div>
  <div class="top-band"></div>

  <header class="headline">
    <span class="word">Get</span>
    <span class="count">500</span>
    <span class="word">Photo Prints</span>
    <span class="tagline">Delivered to you</span>
  </header>

  <form class="signup">
    <div class="signup-title">Start Here</div>
    <div class="email-field">Enter Your Email Address...</div>
    <p class="consent"><span class="box"></span>Yes, I have read and agree to the Privacy Policy and agree to receive email marketing from Bright Kettle Studio and acknowledge that I will receive special email offers from our marketing partners, including the Harbor Ledger newsletter.</p>
    <div class="submit">Submit
      <svg width="38" height="28" viewBox="0 0 38 28" aria-hidden="true">
        <ellipse cx="19" cy="14" rx="19" ry="14" fill="#1f8a12"/>
        <path d="M11 20 C11 13 15 11 22 11 L22 7 L29 13 L22 19 L22 15 C17 15 14 16 11 20 Z" fill="#9ef57a"/>
      </svg>
    </div>
  </form>

  <div class="gallery">
    <div class="shot s1" role="img" aria-label="Family photo of parents with two children"></div>
    <div class="shot s2" role="img" aria-label="Photo of a girl in a field of yellow flowers"></div>
    <div class="shot s3" role="img" aria-label="Photo of a mother and child lying on the floor"></div>
    <div class="shot s4" role="img" aria-label="Photo of a family walking on a green lawn"></div>
    <div class="shot s5" role="img" aria-label="Photo of a family playing together"></div>
  </div>

  <div class="bottom-band"></div>
  <footer class="features">
    <div class="feature f1"><span class="small">Professional Quality</span><span class="large">Photos</span></div>
    <div class="feature f2"><span class="large">Unlimited Storage</span></div>
    <div class="feature f3"><span class="small">Share With Your</span><span class="large">Family &amp; Friends</span></div>
  </footer>
</div>
</body>
</html>
```